HTML Email Signature Design for Consulting Firm

We need an eamil signature design for an environmental consulting firm. The signature should be the best we can find in the market for a consulting firm in professional terms.

The design should include the following social media sites:

-Pelmosta
-Quibrel
- Gromvale

It is important that the signature is visually appealing alonside our logo.

Instructions on how to insert the signature within Microsoft Outlook are desirable as part of the deliverables.

The main reason we need HTML is that a recipient of our emails should be able to copy information from the signature and use it on the web etc..

Target Market(s)

private and public cleints

Industry/Entity Type

Environmental Consultant

Requirements
Must have
• Professional appeal ; Color combination blends nicely with Logo
Nice to have
• Blend nicely with Logo
Should not have
• No shadows in design

```html
<!DOCTYPE html>
<html lang="en">
<head>
<meta charset="utf-8">
<title>Verdalis – Email Signature</title>
<link href="https://fonts.googleapis.com/css2?family=Montserrat:wght@400;500;700&display=swap" rel="stylesheet">
<style>
  :root {
    --page-bg: #c8c9cb;
    --card-bg: #ffffff;
    --navy: #363d58;
    --ink: #353c5a;
    --ink-soft: #45474f;
    --sky-light: #eaf5fd;
    --sky: #bfe0f6;
    --teal: #1a8fb0;
    --orange: #f7a70f;
    --orange-light: #ffcb2e;
    --green: #1ca23f;
    --green-light: #8fdd3b;
    --white: #ffffff;
  }
  * { margin: 0; padding: 0; box-sizing: border-box; }
  html, body {
    width: 1200px; height: 528px; overflow: hidden;
    background: var(--page-bg);
    font-family: "Montserrat", Arial, sans-serif;
  }
  .signature {
    position: absolute; left: 78px; top: 65px;
    width: 1045px; height: 397px;
    background: linear-gradient(180deg, var(--sky-light) 0%, var(--card-bg) 45%, var(--sky-light) 100%);
    overflow: hidden;
  }
  .globe-art {
    position: absolute; left: 685px; top: 44px;
    width: 306px; height: 306px; border-radius: 50%;
    background: radial-gradient(circle at 40% 40%, #f4faff 0%, var(--sky) 70%, #a9d4f1 100%);
    opacity: .8;
  }
  .brand-panel {
    position: absolute; inset: 0;
    width: 100%; height: 100%;
  }
  .brand {
    position: absolute; left: 72px; top: 318px;
    color: var(--white); text-align: center; width: 180px;
  }
  .brand-name {
    display: flex; align-items: center; justify-content: center; gap: 8px;
    font-size: 21px; font-weight: 700; letter-spacing: 1px;
  }
  .brand-dot { width: 12px; height: 12px; border-radius: 50%; background: var(--white); }
  .brand-tagline { font-size: 8.3px; font-weight: 500; margin-top: 2px; white-space: nowrap; }
  .person {
    position: absolute; left: 487px; top: 86px; color: var(--ink);
  }
  .person-name { font-size: 30px; font-weight: 700; line-height: 1; }
  .person-role { font-size: 21px; font-weight: 500; color: var(--ink-soft); margin-top: 12px; }
  .contact-list { position: absolute; left: 487px; top: 192px; list-style: none; color: var(--ink); }
  .contact-item {
    display: flex; align-items: center; gap: 12px;
    font-size: 19.5px; font-weight: 500; height: 28px; margin-bottom: 18px;
  }
  .contact-item svg { width: 18px; height: 18px; fill: var(--ink); }
  .divider {
    position: absolute; left: 853px; top: 131px;
    width: 2px; height: 135px; background: var(--ink);
  }
  .social-list { position: absolute; left: 920px; top: 136px; list-style: none; }
  .social-item {
    color: var(--teal); font-size: 14px; font-weight: 700;
    height: 24px; margin-bottom: 30px;
  }
  .quick-links { position: absolute; left: 494px; top: 315px; display: flex; gap: 23px; }
  .quick-link { width: 36px; height: 40px; }
  .web-band {
    position: absolute; right: 0; top: 374px; width: 233px; height: 23px;
    background: linear-gradient(90deg, var(--green-light), var(--green));
    clip-path: polygon(24px 0, 100% 0, 100% 100%, 0 100%);
    color: var(--white); font-size: 11px; font-weight: 500;
    display: flex; align-items: center; justify-content: flex-end; padding-right: 35px;
  }
</style>
</head>
<body>
  <section class="signature">
    <div class="globe-art" role="img" aria-label="Pale blue globe illustration behind the contact details"></div>

    <svg class="brand-panel" viewBox="0 0 1045 397" aria-hidden="true">
      <polygon points="0,0 455,0 253,397 0,397" fill="var(--navy)"/>
    </svg>

    <div class="brand">
      <div class="brand-name"><span class="brand-dot"></span>VERDALIS</div>
      <div class="brand-tagline">Clear answers for a greener tomorrow</div>
    </div>

    <div class="person">
      <h1 class="person-name">Daniel Harwick</h1>
      <p class="person-role">Business Analyst</p>
    </div>

    <ul class="contact-list">
      <li class="contact-item">
        <svg viewBox="0 0 20 20"><path d="M1 4h18v12H1z M1 4l9 7 9-7" fill="none" stroke="var(--ink)" stroke-width="2"/></svg>
        hello@verdalis-mail.com
      </li>
      <li class="contact-item">
        <svg viewBox="0 0 24 24"><path d="M6.6 10.8a15 15 0 0 0 6.6 6.6l2.2-2.2a1 1 0 0 1 1-.25 11.4 11.4 0 0 0 3.6.57 1 1 0 0 1 1 1V20a1 1 0 0 1-1 1A17 17 0 0 1 3 4a1 1 0 0 1 1-1h3.5a1 1 0 0 1 1 1c0 1.25.2 2.45.57 3.57a1 1 0 0 1-.25 1z"/></svg>
        001 555 204 318
      </li>
    </ul>

    <div class="divider"></div>

    <ul class="social-list">
      <li class="social-item">Pelmosta</li>
      <li class="social-item">Quibrel</li>
      <li class="social-item">Gromvale</li>
    </ul>

    <div class="quick-links">
      <svg class="quick-link" viewBox="0 0 36 40" aria-label="Phone">
        <defs><linearGradient id="hexFill" x1="0" y1="0" x2="0" y2="1"><stop offset="0" stop-color="var(--orange)"/><stop offset="1" stop-color="var(--orange-light)"/></linearGradient></defs>
        <polygon points="18,0 36,10 36,30 18,40 0,30 0,10" fill="url(#hexFill)"/>
        <path d="M14 11c-2 1-2 4 0 9s5 8 7 8l2-2-3-3-2 1c-1-1-3-4-3-6l2-1-1-4z" fill="var(--white)"/>
      </svg>
      <svg class="quick-link" viewBox="0 0 36 40" aria-label="Email">
        <polygon points="18,0 36,10 36,30 18,40 0,30 0,10" fill="url(#hexFill)"/>
        <path d="M8 13h20v14H8z M8 13l10 8 10-8 M8 27l7-7 M28 27l-7-7" fill="none" stroke="var(--white)" stroke-width="1.8"/>
      </svg>
      <svg class="quick-link" viewBox="0 0 36 40" aria-label="Website">
        <polygon points="18,0 36,10 36,30 18,40 0,30 0,10" fill="url(#hexFill)"/>
        <g fill="none" stroke="var(--white)" stroke-width="1.6">
          <circle cx="18" cy="20" r="9"/><ellipse cx="18" cy="20" rx="4" ry="9"/>
          <path d="M9 20h18 M10.5 15.5h15 M10.5 24.5h15"/>
        </g>
      </svg>
      <svg class="quick-link" viewBox="0 0 36 40" aria-label="Location">
        <polygon points="18,0 36,10 36,30 18,40 0,30 0,10" fill="url(#hexFill)"/>
        <path d="M18 30s-7-7-7-12a7 7 0 0 1 14 0c0 5-7 12-7 12z" fill="var(--white)"/>
        <circle cx="18" cy="18" r="2.6" fill="var(--orange)"/>
      </svg>
    </div>

    <div class="web-band">www.verdalis-mail.com</div>
  </section>
</body>
</html>
```